Wellness company needs a label design for a new health product

The name of the product is Verdel Chews and is part of Corvina Well. It allows a person to alkalize and maintain a healthy pH so their body can be at optimal health. This is a new product that will be sold in health professional offices only so it should look professional but have a cutting edge appeal. We are open to color options, keeping in mind we want to look fresh not like everyone else out there. We have the existing logo for Corvina Well already designed that will be needed to be incorporated into the label design. To get the Corvina Well logo either go to www.corvwell.example or I have attached a few files. Please contact me if you need me to send logo. Label will wrap around a bottle which will need to have room for a list of ingredients as well as suggested use.

I added a few examples of lables, the first being too basic, I would like more than that. The next two are examples of lables with added design to give it some interest but keeping it still professional. We are looking for a professional feel with an interesting edge.

A thought might be to have a muted design or soft watermark effect in the background. Thanks for all ideas
Updates

We are happy to inform you that we have guaranteed this project. Look forward to seeing your designs.

Reason: We are extending this projesct because we have guaranteed this project. Look forward to working with you.

Reason: Have not received many designs so we are extending the project. Will update more specific details hope this will help. Appreciate your help, thanks

I added two more labels that we like to give an idea what we are looking for, hope this helps.  Have not received many designs look forward to more, thanks

I added some new ideas, I look forward to seeing more designers ideas.

Reason: Waiting for some changes and possible new designs to make our decision.

Target Market(s)

Health Care profesionals, Chiropractors, Wellness Centers

Industry/Entity Type

Health

Requirements
Must have
• Corvina Well logo
product name: Verdel Chews
Should not have
• No people or animals

```html
<!DOCTYPE html>
<html lang="en">
<head>
<meta charset="UTF-8">
<title>Verdel Chews Label</title>
<link href="https://fonts.googleapis.com/css2?family=Quicksand:wght@400;500&display=swap" rel="stylesheet">
<style>
  :root {
    --backdrop: #736e6c;
    --label: #ffffff;
    --ink: #2b2b2b;
    --ink-soft: #3a3a3a;
    --grid-night: #22152e;
    --grid-lime: #c9c83a;
    --grid-moss: #3d5a2a;
    --grid-deep: #16200f;
  }
  * { margin: 0; padding: 0; box-sizing: border-box; }
  html, body {
    width: 1200px;
    height: 900px;
    overflow: hidden;
    background: var(--backdrop);
    font-family: "Quicksand", sans-serif;
    color: var(--ink);
  }
  .label {
    position: absolute;
    left: 38px;
    top: 234px;
    width: 1123px;
    height: 468px;
    background: var(--label);
  }
  .info-block {
    position: absolute;
    font-size: 14px;
    line-height: 18.8px;
    letter-spacing: 0.4px;
    color: var(--ink-soft);
  }
  .info-block h2 {
    font-weight: 400;
    font-size: 17px;
    letter-spacing: 0.6px;
    margin-bottom: 2px;
    color: var(--ink);
  }
  .ingredients { left: 41px; top: 27px; }
  .directions { left: 44px; top: 252px; }
  .brand {
    position: absolute;
    left: 462px;
    top: 38px;
    width: 220px;
    display: flex;
    align-items: center;
    gap: 8px;
    font-size: 30px;
    font-weight: 500;
    color: var(--ink);
    letter-spacing: 0.3px;
  }
  .brand-square {
    width: 14px;
    height: 14px;
    background: var(--ink);
  }
  .product-name {
    position: absolute;
    left: 0;
    width: 1123px;
    top: 153px;
    text-align: center;
    font-size: 29px;
    font-weight: 400;
    letter-spacing: 0.8px;
    color: var(--ink);
  }
  .hero-art {
    position: absolute;
    left: 441px;
    top: 194px;
    width: 251px;
    height: 221px;
    background: linear-gradient(180deg, var(--grid-night) 0%, var(--grid-night) 28%, var(--grid-lime) 34%, var(--grid-moss) 55%, var(--grid-deep) 100%);
  }
  .net-weight {
    position: absolute;
    left: 0;
    width: 1136px;
    top: 435px;
    text-align: center;
    font-size: 14px;
    letter-spacing: 0.4px;
    color: var(--ink);
  }
  .other-info {
    position: absolute;
    left: 994px;
    top: 30px;
    height: 396px;
    writing-mode: vertical-rl;
    transform: rotate(180deg);
    font-size: 14px;
    line-height: 19px;
    letter-spacing: 0.4px;
    color: var(--ink-soft);
    width: 40px;
  }
</style>
</head>
<body>
  <main class="label">
    <section class="info-block ingredients">
      <h2>Ingredients:</h2>
      <p>sampletextsample</p>
      <p>sampletextsample</p>
      <p>sampletextsample</p>
      <p>sampletextsample</p>
      <p>sampletextsample</p>
      <p>sampletextsample</p>
      <p>sampletextsample</p>
      <p>sampletextsample</p>
      <p>sampletextsample</p>
    </section>

    <section class="info-block directions">
      <h2>How to use:</h2>
      <p>sampletextsample</p>
      <p>sampletextsample</p>
      <p>sampletextsample</p>
      <p>sampletextsample</p>
      <p>sampletextsample</p>
      <p>sampletextsample</p>
      <p>sampletextsample</p>
      <p>sampletextsample</p>
      <p>sampletextsample</p>
    </section>

    <div class="brand"><span class="brand-square"></span><span>Corvina Well</span></div>

    <h1 class="product-name">Verdel Chews</h1>

    <div class="hero-art" role="img" aria-label="Mosaic of small square tiles rising from deep green at the bottom through lime to a dark purple top"></div>

    <p class="net-weight">Net weight 10 oz</p>

    <p class="other-info">Other information: sample, sample, sample, sample, sample, sample, sample, sample, sample, sample.</p>
  </main>
</body>
</html>
```